METAL FABRICATION BUSINESS CARD

** I will be ending the project and picking design early. This Friday October 3rd at 7am MST if not sooner**
ONE SIDED BUSINESS CARD ONLY. AND LOGO SIZE TO BE DOMINANT so it stands out.
Looking for a black background and will be doing raised chrome/silver font on the business cards. Looking to have the following on the front of the business card. Company logo is uploaded in files.
Company logo
*Compartment Doors
*Roof Radius Metal
*J-Wrap Metal Skirting
*S-Lock Beltline Molding
*Pre-Bent Molding
and more...
Owen Daltry 307.552.4198 info@KX-Welt.com
Updates
One sided business card only please. Also logo size should be dominant and sized bigger
Contact Information for Business Card
Black background, Text will be raised chrome/silver, and corners will be rounded.

```html
<!DOCTYPE html>
<html lang="en">
<head>
<meta charset="UTF-8">
<title>KX-Welt Business Card</title>
<link rel="stylesheet" href="https://fonts.googleapis.com/css2?family=Open+Sans:wght@400;600;700&display=swap">
<style>
  :root {
    --page-bg: #101010;
    --card-top: #3d3d3d;
    --card-bottom: #151515;
    --silver: #d4d4d4;
    --silver-soft: #c2c2c2;
    --white: #f4f4f4;
  }
  * { margin: 0; padding: 0; box-sizing: border-box; }
  html, body {
    width: 1200px;
    height: 1059px;
    overflow: hidden;
    background: var(--page-bg);
    font-family: "Open Sans", sans-serif;
  }
  .business-card {
    position: absolute;
    left: 50px;
    top: 215px;
    width: 1100px;
    height: 628px;
    border-radius: 32px;
    background: radial-gradient(ellipse at 45% 0%, var(--card-top) 0%, #262626 45%, var(--card-bottom) 100%);
  }
  .brand-name {
    position: absolute;
    right: 73px;
    top: 78px;
    font-size: 112px;
    font-weight: 700;
    line-height: 1;
    letter-spacing: -1px;
    color: var(--silver);
  }
  .holder-name {
    position: absolute;
    left: 59px;
    top: 365px;
    font-size: 44px;
    font-weight: 600;
    color: var(--white);
  }
  .divider {
    position: absolute;
    left: 59px;
    right: 54px;
    top: 441px;
    height: 3px;
    background: var(--white);
  }
  .contact-list {
    position: absolute;
    left: 59px;
    top: 469px;
    list-style: none;
  }
  .contact-item {
    display: flex;
    align-items: center;
    height: 50px;
    font-size: 29px;
    color: var(--silver-soft);
  }
  .contact-item svg {
    width: 28px;
    height: 28px;
    margin-right: 18px;
    fill: var(--silver-soft);
  }
  .service-list {
    position: absolute;
    right: 54px;
    top: 454px;
    text-align: right;
    font-size: 26px;
    font-weight: 700;
    line-height: 45px;
    color: var(--silver);
  }
</style>
</head>
<body>
  <div class="business-card">
    <div class="brand-name">KX-Welt</div>

    <div class="holder-name">Owen Daltry</div>
    <div class="divider"></div>

    <ul class="contact-list">
      <li class="contact-item">
        <svg viewBox="0 0 24 24" aria-hidden="true"><path d="M6.6 10.8c1.4 2.8 3.8 5.1 6.6 6.6l2.2-2.2c.3-.3.7-.4 1-.2 1.1.4 2.3.6 3.6.6.6 0 1 .4 1 1V20c0 .6-.4 1-1 1C10.6 21 3 13.4 3 4c0-.6.4-1 1-1h3.5c.6 0 1 .4 1 1 0 1.3.2 2.5.6 3.6.1.3 0 .7-.2 1l-2.3 2.2z"/></svg>
        307.552.4198
      </li>
      <li class="contact-item">
        <svg viewBox="0 0 24 24" aria-hidden="true"><path d="M2 5h20v14H2V5zm2 2v.5l8 5 8-5V7H4zm0 2.8V17h16V9.8l-8 5-8-5z"/></svg>
        info@KX-Welt.com
      </li>
    </ul>

    <div class="service-list">
      <div>• Compartment Doors • Roof Radius Metal</div>
      <div>• J-Wrap Metal Skirting • S-Lock Beltline Molding</div>
      <div>• Pre-Bent Molding&nbsp; and more...</div>
    </div>
  </div>
</body>
</html>
```